Valbrina Soletti Winery 2023 Label

We are just about to bottle our very first Napa Valley Cabernet Sauvignon and need label ideas

Target Market(s)

Cab drinkers who like Napa California Cabs

Industry/Entity Type

Wine Making

Logo Text

Valbrina Soletti 2023 Napa Estate Grown Cabernet Sauvignon

Requirements
Must have
• Winery Name, year of vintage and Napa Estate Cab
Nice to have
• If using the initials V and S use gold letters on black or red background

```html
<!DOCTYPE html>
<html lang="en">
<head>
<meta charset="utf-8">
<title>Valbrina Soletti 2023 Estate Grown Cabernet Sauvignon Label</title>
<link href="https://fonts.googleapis.com/css2?family=Poiret+One&family=Josefin+Sans:wght@400;600&display=swap" rel="stylesheet">
<style>
  :root {
    --canvas-bg: #ffffff;
    --label-black: #141414;
    --bronze-light: #b8926a;
    --bronze: #8c6a4b;
    --bronze-dark: #5e4632;
  }
  * { margin: 0; padding: 0; box-sizing: border-box; }
  html, body {
    width: 1200px;
    height: 1200px;
    overflow: hidden;
    background: var(--canvas-bg);
  }
  .canvas {
    width: 1200px;
    height: 1200px;
    display: flex;
    align-items: center;
    justify-content: center;
  }
  .label {
    width: 760px;
    height: 1060px;
    background: var(--label-black);
    display: flex;
    flex-direction: column;
    align-items: center;
    position: relative;
  }
  .bronze-text {
    background: linear-gradient(180deg, var(--bronze-light) 0%, var(--bronze) 55%, var(--bronze-dark) 100%);
    -webkit-background-clip: text;
    background-clip: text;
    color: transparent;
  }
  .vineyard-line {
    margin-top: 92px;
    font-family: "Josefin Sans", sans-serif;
    font-weight: 600;
    font-size: 25px;
    letter-spacing: 0.04em;
    text-transform: uppercase;
  }
  .title-block {
    margin-top: 240px;
    display: flex;
    flex-direction: column;
    align-items: center;
    font-family: "Poiret One", sans-serif;
    text-transform: uppercase;
    line-height: 0.92;
    text-align: center;
  }
  .winery-name {
    font-size: 104px;
    letter-spacing: 0.01em;
  }
  .vintage {
    font-size: 196px;
    line-height: 0.86;
    letter-spacing: 0.02em;
  }
  .estate {
    font-size: 78px;
    letter-spacing: 0.01em;
  }
  .varietal {
    font-family: "Josefin Sans", sans-serif;
    font-size: 50px;
    letter-spacing: 0.01em;
    margin-top: 6px;
  }
  .region {
    position: absolute;
    bottom: 150px;
    font-family: "Josefin Sans", sans-serif;
    font-weight: 600;
    font-size: 30px;
    letter-spacing: 0.04em;
  }
</style>
</head>
<body>
  <main class="canvas">
    <section class="label" aria-label="Wine label">
      <p class="vineyard-line bronze-text">Valbrina Soletti Vineyards</p>
      <div class="title-block">
        <h1 class="winery-name bronze-text">Valbrina<br>Soletti</h1>
        <p class="vintage bronze-text">2023</p>
        <p class="estate bronze-text">Estate Grown</p>
        <p class="varietal bronze-text">Cabernet Sauvignon</p>
      </div>
      <p class="region bronze-text">NAPA</p>
    </section>
  </main>
</body>
</html>
```